New local Orchid nursery branding

We need a business card designed for our small local company in Darwin, Australia that grows orchids, called Blooms at Carrow.
We will be running private sales from our property, and handing these out at local events for perspective customers.

We would like to see designs that are simple, and able to be used with minimal colours and containing an orchid, preferably a stylised representation instead of a photo.
The eventual hope is to take this into larger formats to create our company logo/branding etc, but for now we just need business cards.

Target Market(s)

Local Orchid

Industry/Entity Type

Business

Contact Information for Business Card

Company Name
Logo
Name
Phone Number
Street Address
Email Address (less prominent than rest of the text)

Font styles to use
Sans Serif

Requirements
Must have
• Name of the company, which is Blooms at Carrow
Nice to have
• stylised orchid logo
Should not have
• too many colours

```html
<!DOCTYPE html>
<html lang="en">
<head>
<meta charset="utf-8">
<title>Blooms at Carrow — Business Card</title>
<link rel="stylesheet" href="https://fonts.googleapis.com/css2?family=Josefin+Sans:wght@600&family=Open+Sans:wght@400;600&display=swap">
<style>
  :root {
    --backdrop: #3a3838;
    --card-lilac: #e9d7eb;
    --card-white: #ffffff;
    --plum: #7a3d8c;
    --ink: #222222;
  }
  * { margin: 0; padding: 0; box-sizing: border-box; }
  html, body { width: 1200px; height: 1200px; overflow: hidden; }
  body { background: var(--backdrop); position: relative; font-family: "Open Sans", sans-serif; }

  .card {
    position: absolute;
    width: 720px;
    height: 411px;
    box-shadow: 0 8px 22px rgba(0,0,0,0.35);
  }

  .wordmark {
    position: absolute;
    font-family: "Open Sans", sans-serif;
    font-weight: 600;
    color: var(--plum);
    line-height: 1;
    white-space: nowrap;
  }

  /* Front */
  .card-front { left: 110px; top: 150px; background: var(--card-lilac); }
  .card-front .wordmark { left: 0; right: 0; top: 182px; text-align: center; font-size: 40px; }

  /* Back */
  .card-back { left: 370px; top: 640px; background: var(--card-white); }
  .card-back .wordmark { left: 40px; top: 62px; font-size: 44px; }

  .person { position: absolute; left: 0; right: 0; top: 200px; text-align: center; padding-left: 130px; }
  .person-name { font-family: "Josefin Sans", sans-serif; font-weight: 600; color: var(--plum); font-size: 26px; letter-spacing: 2px; }
  .person-role { font-size: 12px; color: var(--ink); margin-top: 2px; }

  .contact-list { position: absolute; left: 34px; top: 290px; list-style: none; }
  .contact-list li { display: flex; align-items: center; gap: 10px; font-size: 14px; color: var(--ink); height: 22px; }
  .contact-list svg { width: 15px; height: 15px; flex: none; }
  .contact-list .email { font-size: 13px; }

  .address { position: absolute; left: 440px; top: 320px; font-size: 14px; color: var(--ink); line-height: 1.4; font-style: normal; }
</style>
</head>
<body>

<section class="card card-front" aria-label="Card front">
  <p class="wordmark">Blooms at Carrow</p>
</section>

<section class="card card-back" aria-label="Card back">
  <p class="wordmark">Blooms at Carrow</p>

  <div class="person">
    <p class="person-name">DANA WHITLOW</p>
    <p class="person-role">Director</p>
  </div>

  <ul class="contact-list">
    <li>
      <svg viewBox="0 0 16 16" aria-hidden="true"><circle cx="8" cy="8" r="8" fill="var(--plum)"/><path d="M5.2 4.2l1.6-.4.8 2-1 .8a5 5 0 0 0 2.8 2.8l.8-1 2 .8-.4 1.6c-3.8.2-6.8-2.8-6.6-6.6z" fill="#fff"/></svg>
      555.012.4478 x118
    </li>
    <li class="email">
      <svg viewBox="0 0 16 16" aria-hidden="true"><circle cx="8" cy="8" r="8" fill="var(--plum)"/><rect x="4" y="5.2" width="8" height="5.6" fill="#fff"/><path d="M4 5.2l4 3 4-3" fill="none" stroke="var(--plum)" stroke-width="0.9"/></svg>
      dana.whitlow@bloomsatcarrow.ca
    </li>
    <li>
      <svg viewBox="0 0 16 16" aria-hidden="true"><circle cx="8" cy="8" r="8" fill="var(--plum)"/><g fill="none" stroke="#fff" stroke-width="0.9"><circle cx="8" cy="8" r="4.3"/><ellipse cx="8" cy="8" rx="1.8" ry="4.3"/><path d="M3.7 8h8.6"/></g></svg>
      www.bloomsatcarrow.ca
    </li>
  </ul>

  <address class="address">
    74 Palmgrove Road, Ste. 12<br>
    Lakeside, Ontario<br>
    L4K2P9
  </address>
</section>

</body>
</html>
```